Communication and Marketing agency needs a new presentation card

We are a group of communication and marketing agencies specialized in companies that are in the logistics and industrial sector. The head agency is VELUNEX Grupo and the group consists of 4 agencies: VELUNEX Media, VELUNEX Digital, VELUNEX Research and PlanoDeImagenes. We hace 4 offices in Spain (Madrid, Barcelona, Valencia and Murcia). We are looking for a clean and attractive design that transmits our experience, brand presence in the market and knowledge to those who receive the card.It has to maintain the colors of the logo that is attached.
logistics and industrial sector
Marketing department
Clean and attractive design

```html
<!DOCTYPE html>
<html lang="en">
<head>
<meta charset="utf-8">
<title>VELUNEX Grupo – Business Card</title>
<link rel="stylesheet" href="https://fonts.googleapis.com/css2?family=Oswald:wght@500&family=Roboto:wght@400;500&display=swap">
<style>
  :root {
    --brand-red: #b3222b;
    --ink: #4a4a4a;
    --ink-soft: #6b6b6b;
    --rule: #8a8a8a;
    --paper: #ffffff;
    --map-tone: #ededed;
    --stage: #d9d9d9;
  }
  * { box-sizing: border-box; margin: 0; padding: 0; }
  html, body {
    width: 1200px; height: 895px; overflow: hidden;
    background: var(--stage);
    font-family: "Roboto", Arial, sans-serif;
  }
  .card {
    position: absolute; left: 250px;
    width: 700px; height: 400px;
    background: var(--paper);
    border-radius: 26px;
    border-bottom: 4px solid var(--brand-red);
    border-right: 4px solid var(--brand-red);
    box-shadow: 0 6px 18px rgba(0,0,0,.18);
    overflow: hidden;
  }
  .card--back { top: 30px; }
  .card--front { top: 465px; }

  .brand {
    position: absolute; color: var(--brand-red);
    font-family: "Roboto", Arial, sans-serif; font-weight: 500;
    letter-spacing: 3px; line-height: 1;
  }

  /* back */
  .office-map {
    position: absolute; left: 150px; top: 70px;
    width: 330px; height: 290px;
    background: radial-gradient(ellipse at 50% 45%, var(--map-tone) 0%, var(--map-tone) 55%, rgba(237,237,237,0) 72%);
  }
  .card--back .brand { right: 70px; top: 60px; font-size: 54px; }
  .offices {
    position: absolute; right: 70px; top: 140px;
    font-size: 16px; letter-spacing: 3px; color: var(--ink);
  }
  .offices span { color: var(--ink-soft); margin: 0 10px; }
  .agency-rule {
    position: absolute; left: 50px; right: 50px; top: 270px;
    border-top: 1px solid var(--rule);
  }
  .agencies {
    position: absolute; left: 50px; right: 50px; top: 292px;
    display: flex; justify-content: space-between; align-items: baseline;
  }
  .agency {
    color: var(--brand-red); font-weight: 500;
    font-size: 17px; letter-spacing: 1.5px;
  }

  /* front */
  .card--front .brand { right: 60px; top: 50px; font-size: 54px; }
  .rule-line {
    position: absolute; top: 230px; left: 90px; right: 60px; height: 1px;
    background: linear-gradient(to right, var(--rule) 0 52%, var(--brand-red) 52% 100%);
  }
  .address {
    position: absolute; right: 60px; top: 246px;
    text-align: right; font-size: 16px; line-height: 1.4; color: var(--ink);
  }
  .person { position: absolute; left: 90px; top: 170px; }
  .person__name {
    font-family: "Oswald", "Arial Narrow", sans-serif; font-weight: 500;
    font-size: 36px; line-height: 1; color: var(--ink);
  }
  .person__name em { font-style: normal; color: var(--brand-red); }
  .person__role { font-size: 17px; color: var(--ink); margin-top: 4px; }
  .contact-rule {
    position: absolute; left: 90px; top: 258px; width: 190px;
    border-top: 1px solid var(--ink);
  }
  .contacts {
    position: absolute; left: 90px; top: 268px;
    list-style: none; font-size: 16px; line-height: 24px; color: var(--ink);
  }
  .contacts li { display: flex; align-items: center; gap: 10px; }
  .contacts svg { width: 14px; height: 14px; fill: var(--brand-red); flex: none; }
</style>
</head>
<body>

<section class="card card--back">
  <div class="office-map" role="img" aria-label="Faint map of Spain showing the group's offices"></div>
  <div class="brand">VELUNEX Grupo</div>
  <p class="offices">Madrid<span>|</span>Barcelona<span>|</span>Valencia<span>|</span>Murcia</p>
  <div class="agency-rule"></div>
  <div class="agencies">
    <span class="agency">VELUNEX Media</span>
    <span class="agency">VELUNEX Digital</span>
    <span class="agency">VELUNEX Research</span>
    <span class="agency">PlanoDeImagenes</span>
  </div>
</section>

<section class="card card--front">
  <div class="brand">VELUNEX Grupo</div>
  <div class="rule-line"></div>
  <p class="address">4720 N. Harwell PKWY Ste. B<br>Brenford, TX 37412</p>

  <div class="person">
    <h1 class="person__name">Tomás <em>Ribera</em></h1>
    <p class="person__role">Director</p>
  </div>
  <div class="contact-rule"></div>
  <ul class="contacts">
    <li><svg viewBox="0 0 14 14" aria-hidden="true"><rect x="3" y="0" width="8" height="14" rx="1.5"/><rect x="4.5" y="2" width="5" height="8" fill="#fff"/></svg>014 562 3308</li>
    <li><svg viewBox="0 0 14 14" aria-hidden="true"><path d="M3 1l3 3-1.5 2c1 2 2 3 4 4l2-1.5 3 3-2 2C6 13 1 8 1 3z"/></svg>125 870 4416</li>
    <li><svg viewBox="0 0 14 14" aria-hidden="true"><rect x="0" y="2" width="14" height="10" rx="1"/><path d="M1 3l6 5 6-5" stroke="#fff" stroke-width="1.4" fill="none"/></svg>info@velunexgrupo.com</li>
    <li><svg viewBox="0 0 14 14" aria-hidden="true"><circle cx="7" cy="7" r="7"/><path d="M0 7h14M7 0v14M2 3.5h10M2 10.5h10" stroke="#fff" stroke-width="1" fill="none"/></svg>www.velunexgrupo.com</li>
  </ul>
</section>

</body>
</html>
```